front and back labels on a single sheet.

Vodka label design
Vodka is a colourless liquor. This vodka is tasteless and with no flavour.

FRONT LABEL
"FROST TALLY" is the brand name . it should be as big as possible.
below that " Only vodka made from sustainable means"
Remaining details to be copied from attached file.
Back Label
Details attached.

Colors
00AB8E
00BBA5
67D7C9
C6EFE9
E9F9F6

```html
<!DOCTYPE html>
<html lang="en">
<head>
<meta charset="utf-8">
<title>Frost Tally Vodka – Front and Back Labels</title>
<link href="https://fonts.googleapis.com/css2?family=Cinzel:wght@400;600&family=Crimson+Text:wght@400;700&family=Stint+Ultra+Condensed&display=swap" rel="stylesheet">
<style>
  :root {
    --sheet: #ececec;
    --label: #ffffff;
    --ink: #111111;
    --ink-soft: #2a2a2a;
  }
  * { box-sizing: border-box; margin: 0; padding: 0; }
  html, body { width: 1200px; height: 1001px; overflow: hidden; }
  body {
    background: var(--sheet);
    position: relative;
    color: var(--ink);
    font-family: "Crimson Text", Georgia, serif;
  }
  .label {
    position: absolute;
    top: 285px;
    width: 400px;
    height: 430px;
    background: var(--label);
  }
  .label--front { left: 170px; }
  .label--back { left: 630px; }
  .label__rules { position: absolute; inset: 0; width: 400px; height: 430px; }
  .label__text { position: absolute; }
  .centered { left: 0; right: 0; text-align: center; }

  /* Front */
  .seal-name {
    top: 86px;
    font-family: "Cinzel", Georgia, serif;
    font-size: 9px;
    letter-spacing: 1px;
    font-weight: 600;
  }
  .spice-line {
    top: 135px;
    font-family: "Cinzel", Georgia, serif;
    font-size: 19px;
    letter-spacing: 3px;
  }
  .brand-name {
    top: 172px;
    font-family: "Stint Ultra Condensed", "Arial Narrow", serif;
    font-size: 100px;
    line-height: 1;
    letter-spacing: 2px;
    font-weight: 400;
    transform: scaleY(1.05);
  }
  .tagline {
    top: 283px;
    font-size: 12px;
    font-weight: 700;
    letter-spacing: 0.2px;
  }
  .abv, .volume {
    top: 372px;
    width: 100px;
    text-align: center;
    font-family: "Cinzel", Georgia, serif;
    font-size: 14px;
    font-weight: 600;
    letter-spacing: 2px;
  }
  .abv { left: 22px; }
  .volume { right: 22px; }
  .grade {
    top: 348px;
    left: 145px;
    width: 110px;
    text-align: center;
    font-family: "Cinzel", Georgia, serif;
    font-size: 11px;
    line-height: 1.65;
    letter-spacing: 3px;
  }

  /* Back */
  .intro {
    top: 24px;
    left: 18px;
    width: 364px;
    text-align: center;
    font-size: 11.6px;
    line-height: 1.5;
    text-transform: uppercase;
  }
  .intro p + p { margin-top: 5px; }
  .icon-row {
    position: absolute;
    top: 164px;
    left: 0;
    width: 400px;
    height: 50px;
  }
  .serving {
    top: 234px;
    left: 22px;
    width: 158px;
    font-size: 10px;
    line-height: 1.4;
  }
  .serving .contact { margin-top: 10px; }
  .serving .contact strong { display: block; font-weight: 700; }
  .maker {
    top: 230px;
    left: 212px;
    width: 175px;
  }
  .maker__title { font-size: 11px; font-weight: 700; line-height: 1.2; text-transform: uppercase; }
  .maker__name { font-size: 8.5px; line-height: 1.35; text-transform: uppercase; margin-top: 2px; }
  .distillery {
    top: 296px;
    left: 212px;
    width: 78px;
    display: flex;
    align-items: center;
    gap: 5px;
    font-size: 10px;
    font-weight: 700;
    line-height: 1.1;
  }
  .distillery__mark { width: 14px; height: 14px; background: var(--ink); flex: none; }
  .origin {
    top: 290px;
    left: 298px;
    width: 90px;
    font-size: 8.5px;
    line-height: 1.35;
    text-transform: uppercase;
  }
  .origin strong { display: block; font-size: 10px; }
  .source-line {
    top: 378px;
    font-family: "Cinzel", Georgia, serif;
    font-size: 17px;
    letter-spacing: 1px;
  }
</style>
</head>
<body>

<section class="label label--front" aria-label="Front label">
  <svg class="label__rules" viewBox="0 0 400 430" aria-hidden="true">
    <rect x="0" y="4" width="400" height="3" fill="var(--ink)"/>
    <circle cx="200" cy="90" r="36" fill="none" stroke="var(--ink)" stroke-width="2"/>
    <line x1="34" y1="168" x2="366" y2="168" stroke="var(--ink)" stroke-width="1.5"/>
    <polygon points="26,168 34,164 42,168 34,172" fill="var(--ink)"/>
    <polygon points="358,168 366,164 374,168 366,172" fill="var(--ink)"/>
    <line x1="40" y1="270" x2="360" y2="270" stroke="var(--ink)" stroke-width="1.5"/>
    <polygon points="186,270 200,265 214,270 200,275" fill="var(--ink)"/>
    <line x1="40" y1="316" x2="360" y2="316" stroke="var(--ink)" stroke-width="1.5"/>
    <polygon points="186,316 200,311 214,316 200,321" fill="var(--ink)"/>
    <polygon points="136,423 144,423 140,332" fill="var(--ink)"/>
    <polygon points="256,423 264,423 260,332" fill="var(--ink)"/>
    <rect x="0" y="421" width="400" height="3" fill="var(--ink)"/>
  </svg>
  <div class="label__text centered seal-name">FROST TALLY</div>
  <div class="label__text centered spice-line">MADE FROM 5 SPICES</div>
  <h1 class="label__text centered brand-name">FROST TALLY</h1>
  <div class="label__text centered tagline">ONLY VODKA MADE FROM SUSTAINABLE MEANS</div>
  <div class="label__text abv">50%</div>
  <div class="label__text grade">PREMIUM<br>QUALITY<br>VODKA</div>
  <div class="label__text volume">750ML</div>
</section>

<section class="label label--back" aria-label="Back label">
  <svg class="label__rules" viewBox="0 0 400 430" aria-hidden="true">
    <rect x="0" y="4" width="400" height="3" fill="var(--ink)"/>
    <line x1="30" y1="150" x2="370" y2="150" stroke="var(--ink)" stroke-width="1.5"/>
    <polygon points="186,150 200,145 214,150 200,155" fill="var(--ink)"/>
    <line x1="20" y1="222" x2="380" y2="222" stroke="var(--ink)" stroke-width="1.5"/>
    <polygon points="193,226 199,226 196,352" fill="var(--ink)"/>
    <line x1="20" y1="372" x2="380" y2="372" stroke="var(--ink)" stroke-width="1.5"/>
    <line x1="40" y1="406" x2="360" y2="406" stroke="var(--ink)" stroke-width="1.5"/>
    <polygon points="186,406 200,401 214,406 200,411" fill="var(--ink)"/>
    <rect x="0" y="421" width="400" height="3" fill="var(--ink)"/>
  </svg>

  <div class="label__text intro">
    <p>The only vodka in the whole world<br>which has unique 5 spices, and distilled 3+1 times</p>
    <p>In addition this is the only vodka made from natural rainwater &amp; solar power, thus making it the only vodka that is sustainably manufactured.</p>
  </div>

  <svg class="icon-row" viewBox="0 0 400 50">
    <circle cx="85" cy="25" r="20" fill="var(--ink)" role="img" aria-label="Pregnancy warning pictogram"/>
    <g role="img" aria-label="No drinking while pregnant pictogram">
      <circle cx="165" cy="25" r="18.5" fill="none" stroke="var(--ink)" stroke-width="3"/>
      <line x1="152" y1="12" x2="178" y2="38" stroke="var(--ink)" stroke-width="3"/>
    </g>
    <g role="img" aria-label="Glass recycling symbol">
      <polygon points="245,6 266,42 224,42" fill="none" stroke="var(--ink)" stroke-width="2.5" stroke-linejoin="round"/>
      <path d="M242 22 h6 l-1 8 h-4 z" fill="none" stroke="var(--ink)" stroke-width="1.5"/>
    </g>
    <g role="img" aria-label="Standard drinks indicator">
      <path d="M312 6 h26 l-3 38 h-20 z" fill="none" stroke="var(--ink)" stroke-width="1.5"/>
      <text x="325" y="12.5" font-family="Crimson Text, serif" font-size="4" text-anchor="middle" fill="var(--ink)">STD DRINKS</text>
      <rect x="316" y="18" width="18" height="22" fill="var(--ink)"/>
      <text x="325" y="34" font-family="Crimson Text, serif" font-size="12" font-weight="700" text-anchor="middle" fill="var(--label)">27</text>
    </g>
  </svg>

  <div class="label__text serving">
    <p>This vodka has to be taken chilled with ice cubes. Making cocktails with lime and orange is a wonderful experience.</p>
    <p class="contact"><strong>CONTACT AT:</strong>hello@verdantstill.com.au</p>
  </div>

  <div class="label__text maker">
    <div class="maker__title">Fermented<br>and distilled by:</div>
    <div class="maker__name">Aldous M. Renwick<br>at Verdant Still Pvt Ltd</div>
  </div>

  <div class="label__text distillery">
    <span class="distillery__mark"></span>
    <span>Verdant Still</span>
  </div>

  <div class="label__text origin">
    <strong>MADE IN:</strong>
    Kestrel Bay,<br>Victoria,<br>Australia
  </div>

  <div class="label__text centered source-line">MADE FROM SUGARCANE</div>
</section>

</body>
</html>
```